Copper Meadow Creamery Business cards

We need a logo design for our family dairy. Included on the cards should be my name/my husbands name/the dairy name/ all the phone numbers/address and email. The name is Copper Meadow Creamery, LLC. We would like to use our farm mascot pic on the card. We know the pictures I sent you are of a beef cow but she is the mascot of the farm. We were thinking that maybe put a picture of her head in the middle of the card with a "B" on one side and a "D" on the other side with a "C" around the picture of the cow. But we are open to any ideas. We are looking for something kind of professional and a design that that can be used on cards, clothing and a car sign. Black lettering and blue for the other color...or what looks good.

Target Market(s)

All

Industry/Entity Type

Farming

Contact Information for Business Card

Marla Dutton Owner (555)417-2093
Ronald Pfister Owner (555)238-7715
Copper Meadow Creamery, LLC (555)906-4182
Coppermeadowcreamery@mailbarn.test
7126 County Lane 91, Brackenford, IA 50917

Font styles to use
Sans Serif

Colors
3176b5
3c7bb8
3277b5
0255a3

Requirements
Must have
• Some design that incorporates a drawing/pic of the cow pictures that were sent.
Nice to have
• no suggestions
Should not have
• no suggestions

```html
<!DOCTYPE html>
<html lang="en">
<head>
<meta charset="utf-8">
<title>Copper Meadow Creamery – Business Card</title>
<link rel="stylesheet" href="https://fonts.googleapis.com/css2?family=Roboto:wght@400;700&display=swap">
<style>
  :root {
    --backdrop: #f1f1ef;
    --card: #ffffff;
    --brand-blue: #3176b5;
    --soft-blue: #5f8fd0;
    --pale-blue: #cfd9ef;
    --ink: #1c1c1c;
  }
  * { box-sizing: border-box; margin: 0; padding: 0; }
  html, body {
    width: 1200px; height: 848px; overflow: hidden;
    background: var(--backdrop);
    font-family: "Roboto", Arial, sans-serif;
  }
  .business-card {
    position: absolute;
    left: 378px; top: 61px;
    width: 444px; height: 726px;
    background: var(--card);
    box-shadow: 0 2px 10px rgba(0,0,0,0.12);
    text-align: center;
  }
  .brand {
    position: absolute;
    top: 58px; left: 0; right: 0;
    height: 170px;
    display: flex; flex-direction: column;
    align-items: center; justify-content: center;
    gap: 14px;
  }
  .brand-dot {
    width: 96px; height: 96px;
    border-radius: 50%;
    background: var(--pale-blue);
  }
  .brand-name {
    font-weight: 700;
    font-size: 26px;
    color: var(--brand-blue);
  }
  .divider {
    position: absolute;
    top: 271px; left: 54px;
    width: 343px; height: 3px;
    background: var(--brand-blue);
  }
  .contacts {
    position: absolute;
    top: 330px; left: 0; right: 0;
    font-size: 18px;
    line-height: 23px;
  }
  .person { margin-bottom: 20px; }
  .person-name, .company-name {
    font-weight: 700;
    color: var(--ink);
    font-size: 18.5px;
  }
  .person-role, .person-phone, .company-line {
    color: var(--soft-blue);
    font-weight: 400;
  }
  .company { margin-top: 34px; }
  .company-name { margin-bottom: 8px; }
  .company-line { line-height: 31px; }
</style>
</head>
<body>
  <article class="business-card">
    <header class="brand">
      <div class="brand-dot"></div>
      <div class="brand-name">Copper Meadow Creamery</div>
    </header>

    <div class="divider"></div>

    <section class="contacts">
      <div class="person">
        <div class="person-name">Marla Dutton</div>
        <div class="person-role">Owner</div>
        <div class="person-phone">(555)417-2093</div>
      </div>
      <div class="person">
        <div class="person-name">Ronald Pfister</div>
        <div class="person-role">Owner</div>
        <div class="person-phone">(555)238-7715</div>
      </div>
      <div class="company">
        <div class="company-name">Copper Meadow Creamery, LLC</div>
        <div class="company-line">(555)906-4182</div>
        <div class="company-line">Coppermeadowcreamery@mailbarn.test</div>
        <div class="company-line">7126 County Lane 91,</div>
        <div class="company-line">Brackenford, IA 50917</div>
      </div>
    </section>
  </article>
</body>
</html>
```